Real Estate Company Looking for Business Card Designs for 3 Executives

Hello!
Thanks so much for considering our project! We are a real estate investment company located in Edmonton, Alberta called Bellcrane Group of Companies. We invest/develop both commercial and residential real estate and are looking to create 3 DOUBLE-SIDED business cards for 3 top executives in the company! (for some reason it won't let us select the double-sided option, but yes, the cards are double sided and would be happy to tip extra)

We have certain guidelines that we want our business cards to for sure follow - the back of the Business card has to be the Black Background Version of the Logo which has already been designed and linked as a file (first file). We want the entire back of the card to simply just be the black background logo. In terms of the front of the card, would like to see a smaller version of the white background logo (linked as the second file) in the top left hand corner - of course, feel free to get creative and we can make revisions together along the way! and Then after that, just text. We want the card to be sharp, clean, easy on the eyes and highly professional looking. We would like the card to include the Full name of the Company (Bellcrane Group of Companies), Name of the Person, Title, Phone, Email. If possible please provide the front part of the card for 3 people:

1) Bellcrane Group of Companies, Nora Lindqvist, Chief Financial Officer, 780-555-0142, noralindqvist@bellcranegroup.example

2) Bellcrane Group of Companies, Julien Lindqvist, Chief Executive Officer, 780-555-0187, julienlindqvist@bellcranegroup.example

3) Bellcrane Group of Companies, Tom Okafor, Chief Operations Officer, 587-555-0163, tomokafor@bellcranegroup.example

Thank you so much for considering our project & we look forward to seeing your designs!

```html
<!DOCTYPE html>
<html lang="en">
<head>
<meta charset="utf-8">
<title>Bellcrane Group of Companies — Business Card</title>
<link rel="stylesheet" href="https://fonts.googleapis.com/css2?family=Jost:wght@400;500&family=Libre+Baskerville&display=swap">
<style>
  :root {
    --backdrop: #4b4c5c;
    --ink: #111111;
    --paper: #ffffff;
    --card-black: #000000;
    --trunk-dark: #0c0c0c;
  }
  * { margin: 0; padding: 0; box-sizing: border-box; }
  html, body {
    width: 1200px;
    height: 800px;
    overflow: hidden;
  }
  body {
    background: var(--backdrop);
    font-family: "Jost", sans-serif;
    color: var(--ink);
    position: relative;
  }
  .card {
    position: absolute;
    top: 225px;
    width: 540px;
    height: 349px;
    overflow: hidden;
  }

  /* Back of card */
  .card-back {
    left: 45px;
    background: var(--card-black);
    display: flex;
    align-items: center;
    justify-content: center;
  }
  .brand-mark {
    display: flex;
    align-items: center;
    gap: 14px;
    color: var(--paper);
    font-family: "Jost", sans-serif;
    font-weight: 500;
    font-size: 34px;
    letter-spacing: 0.28em;
  }
  .brand-mark .brand-square {
    width: 22px;
    height: 22px;
    background: var(--paper);
  }

  /* Front of card */
  .card-front {
    left: 615px;
    background: var(--paper);
  }
  .front-brand {
    position: absolute;
    left: 36px;
    top: 44px;
    display: flex;
    align-items: center;
    gap: 7px;
    font-weight: 500;
    font-size: 13px;
    letter-spacing: 0.22em;
    color: var(--ink);
  }
  .front-brand .brand-square {
    width: 10px;
    height: 10px;
    background: var(--ink);
  }
  .company-name {
    position: absolute;
    left: 20px;
    width: 210px;
    top: 146px;
    text-align: center;
    font-weight: 500;
    font-size: 20px;
    line-height: 27px;
  }
  .tree-band {
    position: absolute;
    left: 235px;
    top: 0;
    width: 82px;
    height: 100%;
    background: linear-gradient(90deg, #2a2a2a, var(--trunk-dark) 50%, #2a2a2a);
  }
  .contact-block {
    position: absolute;
    left: 330px;
    width: 184px;
    top: 148px;
  }
  .person-name {
    font-weight: 400;
    font-size: 23px;
    line-height: 26px;
    text-align: center;
    white-space: nowrap;
  }
  .person-title {
    font-family: "Libre Baskerville", serif;
    font-size: 7px;
    letter-spacing: 0.18em;
    text-align: center;
    margin-top: 2px;
  }
  .divider {
    display: block;
    margin-top: 24px;
    width: 184px;
    height: 4px;
  }
  .phone {
    margin-top: 12px;
    text-align: right;
    font-size: 9px;
  }
  .email {
    margin-top: 10px;
    text-align: right;
    font-size: 8.6px;
    white-space: nowrap;
  }
</style>
</head>
<body>
  <section class="card card-back" aria-label="Card back">
    <div class="brand-mark">
      <span class="brand-square"></span>
      <span class="brand-name">BELLCRANE</span>
    </div>
  </section>

  <section class="card card-front" aria-label="Card front">
    <div class="front-brand">
      <span class="brand-square"></span>
      <span class="brand-name">BELLCRANE</span>
    </div>

    <p class="company-name">Bellcrane<br>Group of Companies</p>

    <div class="tree-band" role="img" aria-label="Illustration of two tall dark pine tree trunks running the full height of the card"></div>

    <div class="contact-block">
      <p class="person-name">Julien Lindqvist</p>
      <p class="person-title">Chief Executive Officer</p>
      <svg class="divider" viewBox="0 0 184 4" preserveAspectRatio="none" aria-hidden="true">
        <path d="M0 2 Q92 0.4 184 2 Q92 3.6 0 2 Z" fill="#111111"/>
      </svg>
      <p class="phone">780-555-0187</p>
      <p class="email">julienlindqvist@bellcranegroup.example</p>
    </div>
  </section>
</body>
</html>
```